Trucking company needs business card design

New trucking company needs fresh ideas on a business card. Contracted exclusively to Parcelwing, can incorporate their colors or style, but not necessary.
Beckley Haulage, Inc (with or without the Inc.)
Dale Quimby, CEO
801-555-0174
PO BOX 672
Alder, UT

Need to add my email address to the card--beckleyhaulageinc@quillpost.net

Trucking Company

```html
<!DOCTYPE html>
<html lang="en">
<head>
<meta charset="utf-8">
<title>Beckley Haulage – Business Card</title>
<link rel="stylesheet" href="https://fonts.googleapis.com/css2?family=Arimo:wght@400;700&family=Roboto+Condensed:wght@700&family=Tenor+Sans&display=swap">
<style>
  :root {
    --backdrop: #000000;
    --sun: #ffe22c;
    --amber: #ffc21a;
    --tangerine: #ff9800;
    --paper: #ffffff;
    --ink: #000000;
    --charcoal: #333333;
    --gold: #f9b400;
    --ring: #fff25a;
    --badge: #ffae3a;
  }
  * { margin: 0; padding: 0; box-sizing: border-box; }
  html, body {
    width: 1165px; height: 1200px; overflow: hidden;
    background: var(--backdrop);
  }
  .sheet { position: relative; width: 1165px; height: 1200px; }
  .card {
    position: absolute; left: 152px; width: 900px; height: 514px; overflow: hidden;
  }
  .card--front {
    top: 44px;
    background: radial-gradient(ellipse 70% 80% at 45% 45%, var(--sun) 0%, var(--amber) 55%, var(--tangerine) 100%);
  }
  .brand-badge {
    position: absolute; left: 359px; top: 133px; width: 148px; height: 148px;
    border-radius: 50%;
    background: var(--badge);
    border: 14px solid var(--ring);
  }
  .brand-name {
    position: absolute; left: 0; right: 0; top: 318px;
    text-align: center;
    font-family: "Roboto Condensed", "Arial Narrow", sans-serif;
    font-weight: 700; font-size: 102px; line-height: 1;
    font-variant-caps: small-caps;
    letter-spacing: -1px;
    color: var(--ink);
  }
  .card--back { top: 638px; background: var(--paper); }
  .cargo-art { position: absolute; left: 0; top: 0; width: 900px; height: 514px; }
  .holder {
    position: absolute; left: 10px; top: 60px; width: 300px; text-align: right;
  }
  .holder__name {
    font-family: "Tenor Sans", "Trebuchet MS", sans-serif;
    font-size: 56px; line-height: 1; font-weight: 400;
    font-variant-caps: small-caps;
    color: var(--gold);
  }
  .holder__role {
    margin-top: 4px;
    font-family: "Arimo", Arial, sans-serif; font-weight: 700;
    font-size: 35px; line-height: 1; color: var(--charcoal);
  }
  .contact {
    position: absolute; left: 30px;
    display: flex; align-items: center; gap: 22px;
    font-family: "Arimo", Arial, sans-serif; color: var(--ink);
  }
  .contact__icon { width: 17px; height: 17px; flex: none; }
  .contact--phone { top: 280px; font-size: 37px; letter-spacing: 2px; }
  .contact--post { top: 344px; font-size: 36px; line-height: 42px; letter-spacing: 1px; }
  .contact--mail { top: 443px; font-size: 35px; }
</style>
</head>
<body>
<main class="sheet">
  <section class="card card--front">
    <div class="brand-badge"></div>
    <h1 class="brand-name">Beckley Haulage</h1>
  </section>

  <section class="card card--back">
    <svg class="cargo-art" viewBox="0 0 900 514" role="img" aria-label="Stacked yellow and orange 3D cargo cubes">
      <defs>
        <linearGradient id="cargoTone" x1="0" y1="0" x2="1" y2="1">
          <stop offset="0" stop-color="#ffe92e"/>
          <stop offset="0.55" stop-color="#ffbf12"/>
          <stop offset="1" stop-color="#f08a00"/>
        </linearGradient>
      </defs>
      <polygon fill="url(#cargoTone)" points="350,205 377,60 600,60 628,0 900,0 900,514 700,514 680,470 520,430 525,320 470,280"/>
    </svg>

    <div class="holder">
      <h2 class="holder__name">Dale Quimby</h2>
      <p class="holder__role">CEO</p>
    </div>

    <p class="contact contact--phone">
      <svg class="contact__icon" viewBox="0 0 17 17" aria-hidden="true">
        <rect width="17" height="17" fill="#ffc000"/>
        <path d="M5 3 L7 3 L8 6 L6.5 7 Q8 10 10 11 L11 9.5 L14 10.5 L14 12.5 Q13 14 11 14 Q4 12 3 5 Q3 3.5 5 3Z" fill="#000"/>
      </svg>
      <span>801-555-0174</span>
    </p>
    <p class="contact contact--post">
      <svg class="contact__icon" viewBox="0 0 17 17" aria-hidden="true">
        <rect width="17" height="17" fill="#ffc000"/>
        <path d="M8.5 3 A3.5 3.5 0 0 1 12 6.5 Q12 9 8.5 14 Q5 9 5 6.5 A3.5 3.5 0 0 1 8.5 3Z" fill="#000"/>
        <circle cx="8.5" cy="6.5" r="1.3" fill="#ffc000"/>
      </svg>
      <span>PO BOX 672<br>Alder, UT</span>
    </p>
    <p class="contact contact--mail">
      <svg class="contact__icon" viewBox="0 0 17 17" aria-hidden="true">
        <rect width="17" height="17" fill="#ffc000"/>
        <rect x="3" y="5" width="11" height="7.5" fill="#000"/>
        <path d="M3 5 L8.5 9 L14 5" fill="none" stroke="#ffc000" stroke-width="1.2"/>
      </svg>
      <span>beckleyhaulageinc@quillpost.net</span>
    </p>
  </section>
</main>
</body>
</html>
```